Business Card Design for general contractor or developer

General Contractors. We build new buildings as well as redesign and/or remodel existing buildings. Mostly residential, but we want to expand to commercial as well, so we want the design not to be residential specific.We want the design to be modern, but necessarily minimalistic. A monogram type is also a consideration, but would like to see all ideas.

Target Market(s)

Real estate investors, homeowners, future homeowners, commercial building owners

Industry/Entity Type

Contractor

Contact Information for Business Card

BRIMCOVE Developers Corp, 2917 NE 88th Avenue Suite 412 Coral Springs, FL 33071, Darren Kopec, (305) 555-0148, darren@brimcovedev.example

Font styles to use
Other font styles liked:
• Modern type font

Requirements
Must have
• Must be modern looking
Nice to have
• Metallic type or a standout feature
Should not have
• Tools, floorplans

```html
<!DOCTYPE html>
<html lang="en">
<head>
<meta charset="utf-8">
<title>BRIMCOVE Developers Corp – Business Card</title>
<link href="https://fonts.googleapis.com/css2?family=Roboto:wght@400;500&display=swap" rel="stylesheet">
<style>
  :root {
    --brand-blue: #23478f;
    --band-dark: #262626;
    --ink: #1e1e1e;
    --paper: #ffffff;
    --stage: #e9e7e3;
    --mark-ring: #1c1c1c;
  }
  * { margin: 0; padding: 0; box-sizing: border-box; }
  html, body {
    width: 1200px; height: 892px; overflow: hidden;
    background: var(--stage);
    font-family: "Roboto", Arial, sans-serif;
  }
  .sheet { position: relative; width: 1200px; height: 892px; }
  .card {
    position: absolute; top: 292px;
    width: 540px; height: 308px;
    background: var(--paper);
    box-shadow: 0 4px 14px rgba(0,0,0,.18);
    overflow: hidden;
  }
  .card--front { left: 40px; }
  .card--back { left: 620px; }

  .brand-dot {
    position: absolute;
    border-radius: 50%;
    background: var(--brand-blue);
    border: 5px solid var(--mark-ring);
    box-shadow: 0 0 0 3px var(--paper);
  }
  .brand-name {
    color: var(--brand-blue);
    font-weight: 500;
    letter-spacing: .2px;
    white-space: nowrap;
  }

  /* front */
  .card--front .brand-dot { left: 26px; top: 16px; width: 104px; height: 104px; z-index: 2; }
  .card--front .brand-name { position: absolute; left: 148px; top: 52px; font-size: 28px; }
  .address-band {
    position: absolute; left: 0; right: 0; top: 104px; height: 56px;
    background: var(--band-dark);
    border-top: 3px solid var(--paper);
    border-bottom: 3px solid var(--paper);
    box-shadow: 0 -2px 0 var(--brand-blue), 0 2px 0 var(--brand-blue);
    color: #f2f2f2;
    font-size: 14px; line-height: 18px;
    text-align: right;
    padding: 8px 24px 0 0;
  }
  .person { position: absolute; left: 40px; top: 196px; }
  .person__name { color: var(--brand-blue); font-size: 28px; font-weight: 400; }
  .person__title { color: var(--ink); font-size: 13px; margin-top: 2px; }
  .divider {
    position: absolute; left: 262px; top: 186px; width: 3px; height: 92px;
    background: var(--brand-blue);
  }
  .contacts {
    position: absolute; left: 286px; top: 206px;
    list-style: none; color: var(--ink); font-size: 15px;
  }
  .contacts li { display: flex; align-items: center; gap: 10px; height: 30px; white-space: nowrap; }
  .contacts svg { width: 18px; height: 16px; flex: none; }

  /* back */
  .back-lockup {
    position: absolute; left: 24px; top: 178px; width: 370px;
    text-align: right;
  }
  .card--back .brand-name { font-size: 26px; }
  .card--back .email { margin-top: 8px; font-size: 14px; color: var(--ink); }
  .card--back .brand-dot { left: 412px; top: 160px; width: 100px; height: 100px; }
</style>
</head>
<body>
<main class="sheet">
  <section class="card card--front" aria-label="Business card front">
    <span class="brand-dot" aria-hidden="true"></span>
    <h1 class="brand-name">BRIMCOVE Developers Corp</h1>
    <p class="address-band">2917 NE 88th Avenue Suite 412 Coral Springs,<br>FL 33071, Darren Kopec</p>
    <div class="person">
      <p class="person__name">Employee name</p>
      <p class="person__title">Managing Director</p>
    </div>
    <span class="divider" aria-hidden="true"></span>
    <ul class="contacts">
      <li>
        <svg viewBox="0 0 18 16" aria-hidden="true"><rect width="18" height="16" rx="2" fill="#23478f"/><path d="M5 3.5c-1 1 0 4.5 3 7.2s5.5 3 6.3 2l-1.6-2-1.6.8c-1-.5-2.6-2-3.2-3.2l.8-1.5z" fill="#fff"/></svg>
        (305) 555-0148
      </li>
      <li>
        <svg viewBox="0 0 18 16" aria-hidden="true"><rect width="18" height="16" rx="2" fill="#23478f"/><rect x="3.5" y="4" width="11" height="8" fill="none" stroke="#fff" stroke-width="1.3"/><path d="M3.5 4l5.5 4.5L14.5 4" fill="none" stroke="#fff" stroke-width="1.3"/></svg>
        darren@brimcovedev.example
      </li>
    </ul>
  </section>

  <section class="card card--back" aria-label="Business card back">
    <div class="back-lockup">
      <h2 class="brand-name">BRIMCOVE Developers Corp</h2>
      <p class="email">darren@brimcovedev.example</p>
    </div>
    <span class="brand-dot" aria-hidden="true"></span>
  </section>
</main>
</body>
</html>
```